Business card design needed

The company name is Pellwick Architects. We are an architectural company based in Melbourne,Australia that has a mix of client base from health care, commercial office, aged care, multi-residential, single residential and retail. Design type is contemporary.

Suggest the base colours need to be black and white. Please leave an area on the back of the card available for handwritten notes.

Target Market(s)

Generally corporate, aged 30 to 65

Industry/Entity Type

Residential

Contact Information for Business Card

Pellwick Architects
Dane Pellwick
7 Horbury Street
Northvale VIC 3059
T (03) 9572 4016
M 0431 607 295
E dp@pellwickarc.com.au

Logo Text

PA

Logo styles of interest
Emblem Logo
Abstract Logo
Lettermark Logo
Requirements
Must have
• I am having trouble attaching a sketch so would really appreciate your effort to try the following brief.

Black and White (B&W)
Would like different card cutout profile. Logo Example, use the half circle curve of the G to form the left edge of the card with no margin. The A is to sit inside the G, connected to the G by its horizontal. The A has its cross bar and lower right leg removed. Card in black, text in white.

Back of card to be black text on white background with services provided.

Client Focused Service
Architecture and Design
Functional Planning
Town Planning
Feasability Studies
Contract Documentation
Contract Administration
Project Management

Simple elegant text, Ariel or similar
Nice to have
• Integrated logo and card cut-out.

Card base black on front, white on back
Should not have
• Too many colours
Fussy details

```html
<!DOCTYPE html>
<html lang="en">
<head>
<meta charset="utf-8">
<title>Pellwick Architects – Business Card</title>
<link rel="stylesheet" href="https://fonts.googleapis.com/css2?family=Josefin+Sans:wght@300;400&display=swap">
<style>
  :root {
    --backdrop: #2b2b2b;
    --card: #0b0b0b;
    --card-edge: #1c1c1c;
    --ink: #f2f2f2;
    --ink-soft: #d6d6d6;
    --mark: #3a3a3a;
  }
  html, body {
    margin: 0;
    padding: 0;
    width: 1200px;
    height: 1000px;
    overflow: hidden;
    background: var(--backdrop);
  }
  .canvas {
    position: relative;
    width: 1200px;
    height: 1000px;
  }
  .card {
    position: absolute;
    left: 150px;
    top: 225px;
    width: 900px;
    height: 550px;
    background: var(--card);
    border: 1px solid var(--card-edge);
    box-sizing: border-box;
    font-family: "Josefin Sans", "Futura", sans-serif;
    color: var(--ink);
  }
  .brand {
    position: absolute;
    left: 70px;
    top: 150px;
    display: flex;
    align-items: center;
    gap: 22px;
  }
  .brand-dot {
    width: 34px;
    height: 34px;
    border-radius: 50%;
    background: var(--mark);
  }
  .brand-name {
    font-weight: 400;
    font-size: 40px;
    letter-spacing: 1px;
    color: var(--mark);
  }
  .contact {
    position: absolute;
    left: 560px;
    top: 300px;
  }
  .contact-name {
    font-weight: 400;
    font-size: 28px;
    margin: 0 0 14px;
  }
  .contact-lines {
    list-style: none;
    margin: 0;
    padding: 0 0 0 18px;
    font-weight: 300;
    font-size: 15px;
    line-height: 32px;
    color: var(--ink-soft);
  }
</style>
</head>
<body>
<main class="canvas">
  <section class="card" aria-label="Business card front">
    <div class="brand">
      <span class="brand-dot"></span>
      <span class="brand-name">Pellwick Architects</span>
    </div>
    <div class="contact">
      <p class="contact-name">Dane Pellwick</p>
      <ul class="contact-lines">
        <li>7 Horbury Street Northvale VIC 3059</li>
        <li>T. (03) 9572 4016</li>
        <li>M. 0431 607 295</li>
        <li>E. dp@pellwickarc.com.au</li>
      </ul>
    </div>
  </section>
</main>
</body>
</html>
```